Poster design for Chattanooga, TN's 175th Anniversary. Here is a link to our website www.lmw482.org.

Basically, this is a weeklong celebration of community-sourced events highlighting mostly our city's past. Pellworth Tilly Tram (railroads) are big in our past, and we are identified by our river and surrounded by mountains. The week will have a variety of different events so we need to drive people to our website as events will be added continually.

Also, this event is being put on by our local Mayor's office. While we are young and progressive, can't be too crazy or out there. I was thinking more like a throwback concert photo, a la Brindle Loft Presses (famous in Nashville). That would help tie in the vintage vibe.

Reason: I need to provide my comm team with designs next week. This will give everyone the weekend to be creative!

Target Market(s)

Local Chattanooga Residents - kids, young people, older people.

Requirements
Must have
• (website) LMW482.org
• (Date) November 8 - November 15, 2014
Nice to have
• Flag (doesn't matter the treatment)
• "Weeklong Celebration"
• "Community-Sourced Events"
• Logo (doesn't matter the treatment)
• 175 years of Chattanooga
• Stars
Should not have
• any kind of vulgar image or language.
• Should not be pink or purple or neon.

```html
<!DOCTYPE html>
<html lang="en">
<head>
<meta charset="utf-8">
<title>Celebrating 175 Years of Chattanooga</title>
<link rel="stylesheet" href="https://fonts.googleapis.com/css2?family=Oswald:wght@400;500;600&family=Playfair+Display:wght@700;800&display=swap">
<style>
  :root {
    --backdrop: #000000;
    --navy: #1f3462;
    --navy-deep: #162849;
    --cream: #ecebd9;
    --cream-shade: #cfcdb8;
    --red: #b31f24;
  }
  html, body {
    margin: 0;
    padding: 0;
    width: 1200px;
    height: 1000px;
    overflow: hidden;
    background: var(--backdrop);
  }
  .stage { display: block; width: 1200px; height: 1000px; }
  .headline { font-family: "Oswald", sans-serif; font-weight: 500; fill: var(--cream); }
  .serif-title { font-family: "Playfair Display", serif; font-weight: 800; fill: var(--cream); }
  .tagline { font-family: "Oswald", sans-serif; font-weight: 400; fill: var(--cream); }
  .tagline .strong { font-weight: 600; }
  .schedule { font-family: "Oswald", sans-serif; font-weight: 400; fill: var(--navy); }
  .schedule .strong { font-weight: 600; }
  .dates { font-family: "Oswald", sans-serif; font-weight: 500; fill: var(--cream); }
  .star-solid { fill: var(--navy); }
  .star-outline { fill: none; stroke: var(--navy); stroke-width: 0.13; stroke-linejoin: miter; }
  .star-cream { fill: var(--cream); }
  .rule { fill: var(--cream); }
</style>
</head>
<body>
<svg class="stage" viewBox="0 0 1200 1000" xmlns="http://www.w3.org/2000/svg">
  <defs>
    <symbol id="star" viewBox="-1 -1 2 2" overflow="visible">
      <polygon points="0,-1 0.225,-0.309 0.951,-0.309 0.363,0.118 0.588,0.809 0,0.382 -0.588,0.809 -0.363,0.118 -0.951,-0.309 -0.225,-0.309"/>
    </symbol>
    <linearGradient id="locomotive-tone" x1="0" y1="0" x2="1" y2="1">
      <stop offset="0" stop-color="#3c4d74"/>
      <stop offset="0.45" stop-color="#8e92a0"/>
      <stop offset="1" stop-color="#22365f"/>
    </linearGradient>
  </defs>

  <!-- poster sheet -->
  <g class="poster">
    <rect x="268" y="0" width="648" height="1000" fill="var(--navy)"/>

    <!-- top star band -->
    <rect x="268" y="0" width="648" height="58" fill="var(--cream)"/>
    <g class="star-row">
      <use href="#star" class="star-outline" x="-1" y="-1" width="2" height="2" transform="translate(318 35) scale(15)"/>
      <use href="#star" class="star-solid" x="-1" y="-1" width="2" height="2" transform="translate(379 35) scale(15)"/>
      <use href="#star" class="star-outline" x="-1" y="-1" width="2" height="2" transform="translate(440 35) scale(15)"/>
      <use href="#star" class="star-solid" x="-1" y="-1" width="2" height="2" transform="translate(501 35) scale(15)"/>
      <use href="#star" class="star-outline" x="-1" y="-1" width="2" height="2" transform="translate(562 35) scale(15)"/>
      <use href="#star" class="star-solid" x="-1" y="-1" width="2" height="2" transform="translate(623 35) scale(15)"/>
      <use href="#star" class="star-outline" x="-1" y="-1" width="2" height="2" transform="translate(684 35) scale(15)"/>
      <use href="#star" class="star-solid" x="-1" y="-1" width="2" height="2" transform="translate(745 35) scale(15)"/>
      <use href="#star" class="star-outline" x="-1" y="-1" width="2" height="2" transform="translate(806 35) scale(15)"/>
      <use href="#star" class="star-solid" x="-1" y="-1" width="2" height="2" transform="translate(867 35) scale(15)"/>
    </g>

    <!-- headline block -->
    <text class="headline" x="298" y="180" font-size="140" textLength="588" lengthAdjust="spacingAndGlyphs">CELEBRATING</text>
    <text class="serif-title" x="300" y="230" font-size="48" textLength="586" lengthAdjust="spacingAndGlyphs">175 YEARS OF CHATTANOOGA</text>

    <rect class="rule" x="268" y="240" width="62" height="10"/>
    <rect class="rule" x="858" y="240" width="58" height="10"/>
    <text class="tagline" x="342" y="253" font-size="18" textLength="502" lengthAdjust="spacingAndGlyphs">WEEK-LONG CELEBRATION OF COMMUNITY-SOURCED EVENTS</text>

    <!-- hero illustration area -->
    <rect class="hero-art" x="268" y="278" width="648" height="422" fill="url(#locomotive-tone)" role="img" aria-label="Vintage steam locomotive on tracks in front of mountains and river, printed in cream on navy"/>

    <!-- description -->
    <text class="tagline" x="300" y="746" font-size="24" textLength="584" lengthAdjust="spacingAndGlyphs"><tspan class="strong">LMW482 EVENT</tspan> WILL BE SHOWCASING THE UNIQUE HISTORY &amp; CULTURE OF</text>
    <text class="serif-title" x="300" y="793" font-size="46" textLength="310" lengthAdjust="spacingAndGlyphs">CHATTANOOGA</text>
    <text class="tagline" x="618" y="771" font-size="19" textLength="266" lengthAdjust="spacingAndGlyphs">A CELEBRATION FOR <tspan class="strong">ALL</tspan> OUR CITIZENS!!!</text>
    <rect class="rule" x="618" y="778" width="266" height="2.5"/>
    <rect class="rule" x="618" y="785" width="266" height="2.5"/>
    <rect class="rule" x="618" y="792" width="266" height="2.5"/>

    <!-- website band -->
    <rect x="268" y="812" width="648" height="50" fill="var(--cream)"/>
    <text class="schedule" x="302" y="846" font-size="25" textLength="582" lengthAdjust="spacingAndGlyphs">VISIT <tspan class="strong">LMW482.ORG</tspan> FOR A FULL SCHEDULE OF EVENTS</text>

    <!-- date band -->
    <rect x="268" y="862" width="648" height="138" fill="var(--red)"/>
    <use href="#star" class="star-cream" x="-1" y="-1" width="2" height="2" transform="translate(328 932) scale(27)"/>
    <use href="#star" class="star-cream" x="-1" y="-1" width="2" height="2" transform="translate(856 932) scale(27)"/>
    <text class="dates" x="368" y="955" font-size="60" textLength="448" lengthAdjust="spacingAndGlyphs">NOVEMBER 8TH - 15TH</text>
  </g>
</svg>
</body>
</html>
```